Business Stationary, Letterhead, Fax Cover Sheet, Client Intake, Email Signature, Thank you cards.
Marwick Law Firm
Business Stationary, Letterhead, Fax Cover Sheet, Client Intake, Email Signature, Thank you cards. - Law
Creative Brief
Professional
Len Marwick
Lawyer
2837 Falbrook St., Suite 1940 Houston, Texas 77014
len@marwick-law.example
www.marwick-law.example
Please note this project is Not for just One Person but for All Staff. The files should be in editable format to allow for different names and titles on cards.

```html
<!DOCTYPE html>
<html lang="en">
<head>
<meta charset="utf-8">
<title>Marwick Law Firm – Business Cards</title>
<link href="https://fonts.googleapis.com/css2?family=Arimo:ital,wght@0,400;0,700;1,400&display=swap" rel="stylesheet">
<style>
  :root {
    --page-bg: #e9e9ec;
    --card-white: #ffffff;
    --card-black: #050507;
    --blue-light: #4a55ff;
    --blue-mid: #2a2ee0;
    --blue-deep: #12148a;
    --silver: #d7dbe6;
    --navy: #1c2470;
    --text-light: #ffffff;
  }
  * { margin: 0; padding: 0; box-sizing: border-box; }
  html, body { width: 1200px; height: 550px; overflow: hidden; }
  body {
    background: var(--page-bg);
    font-family: "Arimo", Arial, sans-serif;
    display: flex;
    align-items: center;
    justify-content: center;
    gap: 40px;
  }
  .card {
    position: relative;
    width: 540px;
    height: 310px;
    border-radius: 16px;
    overflow: hidden;
    box-shadow: 0 4px 14px rgba(0,0,0,0.18);
  }
  .card--light { background: var(--card-white); }
  .card--dark { background: var(--card-black); }
  .card__swoosh { position: absolute; inset: 0; width: 100%; height: 100%; }
  .brand {
    position: absolute;
    left: 16px;
    width: 200px;
    top: 100px;
    display: flex;
    flex-direction: column;
    align-items: center;
    gap: 10px;
  }
  .brand__dot {
    width: 18px; height: 18px; border-radius: 50%;
    background: var(--blue-mid);
  }
  .brand__name {
    font-weight: 700;
    font-size: 20px;
    letter-spacing: 0.3px;
    white-space: nowrap;
    color: var(--navy);
  }
  .card--dark .brand__name { color: var(--blue-light); }
  .contact {
    position: absolute;
    right: 24px;
    top: 92px;
    text-align: right;
    color: var(--text-light);
  }
  .contact__name { font-size: 17px; font-weight: 700; }
  .contact__title { font-size: 11px; font-style: italic; margin-top: 2px; }
  .contact__address { font-size: 10px; line-height: 1.35; margin-top: 20px; }
  .contact__lines { font-size: 10px; line-height: 1.35; margin-top: 4px; }
  .contact__lines b { font-weight: 700; }
  .contact__lines .gap { margin-top: 4px; }
</style>
</head>
<body>

  <article class="card card--light">
    <svg class="card__swoosh" viewBox="0 0 540 310" aria-hidden="true">
      <defs>
        <linearGradient id="blueFillA" x1="0" y1="0" x2="1" y2="1">
          <stop offset="0" stop-color="var(--blue-light)"/>
          <stop offset="0.55" stop-color="var(--blue-mid)"/>
          <stop offset="1" stop-color="var(--blue-deep)"/>
        </linearGradient>
      </defs>
      <path d="M322 0 C 270 80, 232 200, 250 310 L540 310 L540 0 Z" fill="var(--silver)"/>
      <path d="M338 0 C 286 80, 248 200, 264 310 L540 310 L540 0 Z" fill="url(#blueFillA)"/>
    </svg>
    <div class="brand">
      <span class="brand__dot"></span>
      <span class="brand__name">Marwick Law Firm</span>
    </div>
    <div class="contact">
      <p class="contact__name">Len Marwick</p>
      <p class="contact__title">Lawyer</p>
      <p class="contact__address">2837 Falbrook St., Suite 1940<br>Houston, Texas 77014</p>
      <div class="contact__lines">
        <p><b>Phone:</b> 713-555-0142</p>
        <p><b>Fax:</b> 713-555-0187</p>
        <p class="gap"><b>Email:</b> len@marwick-law.example</p>
        <p><b>Web:</b> www.marwick-law.example</p>
      </div>
    </div>
  </article>

  <article class="card card--dark">
    <svg class="card__swoosh" viewBox="0 0 540 310" aria-hidden="true">
      <defs>
        <linearGradient id="blueFillB" x1="0" y1="0" x2="1" y2="1">
          <stop offset="0" stop-color="var(--blue-light)"/>
          <stop offset="0.55" stop-color="var(--blue-mid)"/>
          <stop offset="1" stop-color="var(--blue-deep)"/>
        </linearGradient>
      </defs>
      <path d="M322 0 C 270 80, 232 200, 250 310 L540 310 L540 0 Z" fill="var(--silver)"/>
      <path d="M338 0 C 286 80, 248 200, 264 310 L540 310 L540 0 Z" fill="url(#blueFillB)"/>
    </svg>
    <div class="brand">
      <span class="brand__dot"></span>
      <span class="brand__name">Marwick Law Firm</span>
    </div>
    <div class="contact">
      <p class="contact__name">Len Marwick</p>
      <p class="contact__title">Lawyer</p>
      <p class="contact__address">2837 Falbrook St., Suite 1940<br>Houston, Texas 77014</p>
      <div class="contact__lines">
        <p><b>Phone:</b> 713-555-0142</p>
        <p><b>Fax:</b> 713-555-0187</p>
        <p class="gap"><b>Email:</b> len@marwick-law.example</p>
        <p><b>Web:</b> www.marwick-law.example</p>
      </div>
    </div>
  </article>

</body>
</html>
```